New website for Scuba Diving School ‘FinWaveX’ in Dublin, Ireland

New website for Scuba Diving School ‘FinWaveX’ based in Dublin, Ireland.

GENERAL DESCRIPTION OF WHAT I WANT THIS WEBSITE TO BE:

Website must be professional and modern looking. It has to be user friendly so that everybody can easily find information they are looking for. I would like to see the site being innovative and funky yet still appeal to the main market which is 25-35 years old with 2/3 being male middle to high income.

Site should be creative with bright colours. As the site is for scuba diving school it should be cheerful and welcoming. Colours should be eye catching and worm to create friendly image from a very first time it’s visited. Images used in the website should stay as realistic as possible yet professional.

Home Page:
Section 1) Left up to you if you want anything above the menu bar.

Section 2) Under need I want to have menu bar that will have 6 main pages and 6 subpages. How you designed the menu bar is up to you as long as you stick the correct content:

Main Page 1. Home
Main Page 2. About Us
Main Page 3. Courses & Prices
Sub Page - Try a Dive Evening
Sub Page - Scuba Review
Sub Page - Beginners Course
Sub Page - Advanced Open water
Sub Page - Rescue Diver
Sub Page - DiveMaster Course
Main Page 4. Contact Us
Main Page 5. FAQ
Main Page 6. Calendar

Section 3)
I would like to stick to minimum text content on the main page but I would like to see the following:

Under the menu bar please create an image slide show that will change every couple of seconds or can be operated by user when clicked on dot, number or arrow. Example can be found on the fallowing website: http://www.brightgrid.example/?tv or http://www.norva.example/scuba/ this is just to give you an idea. I want this slide show to be creative and promote all courses one by one. Pictures in the slide show must be relevant and professional. On each slide please use exact content provided below:

- 1st slide. Content: "Try a Dive Evening for ONLY 49€'
- 2nd slide Content: “Sign up Today for your Beginners Course"
- 3rd slide Content: "Norva Advanced Diver Course"
- 4th slide Content: "The Norva Rescue Diver Course"
- 5th slide Content: "SnapFin with Norva DiveMaster course"

Please link those slides with appropriate course pages so the user can be redirected directly to the course page.

Section 4)
On the bottom of the page I would like to see all links in columns in small print with my logo in the right bottom corner. Please make the logo clearly visible

ADDITIONAL INFORMATION:

Also, somewhere on the page I would like to see some form of a price tag that will attract user attention. The purpose of this price tag is for the user to click on it to check our discounts.

Content for the Price Tag: “MATES RATES 10%OFF” and when clicked it will bring up a pop up window that will state the following:
POP UP Content:

“Sign up now for our next "Try a Dive Evening" and get 10% when you come with your friend! Bring two friends and get 10% off of your next Beginners course"!
Contact us now to book your place!

‘Contact us’ should be a link that will redirect user to the ‘Contact Us’ Page. (This should be done on all pages) plus the link to the calendar page.

About us Page:

Section 1 and Section 2 from the home page should be repeated.

Section 3) Content:

This section will be information to give a customer overview of who we are and what we do. I will provide you with the picture in the next 3-4 day (waiting for the photographer to get back to me) which I would like to be included on this page with fallowing information: Tomas Kelvry Norva No. 584731.
Also I would like this picture to be part of the fallowing content:
Please stick to exact wording:

Content:
Welcome to FinWaveX

We are Dublin based scuba diving school dedicated to teaching Scuba Diving in the internationally recognised NORVA diving system. We have a real passion for diving and love everything about the real magic that the underwater world has to offer.

We teach a range of courses starting from a very beginning right through to professional level diving. All our staffs are official Scuba Diving NORVA, MLS instructors and NORVA DiveMasters.

We take great pride in our professional approach to diving and can guarantee that that you will receive the highest level of expertise and attention available whether you are trying just one evening of scuba or completing your Dive Master program.

FinWaveX is a progressive Eco minded business promoting safe and responsible diving. In everything we do. Everybody who learns to scuba dive with us is taught that safety is at the heart of everything we do in Scuba. The whole worlds of the oceans are opened up to be discovered. We believe that we can all make a huge difference in keeping our oceans healthy and self-sustaining for the generations to come.

Meet our owner and NORVA qualified Instructor at FinWaveX.

“I am originally from Poland but moved to Ireland in 2006 and yes I have a Dublin accent now! When I started my adventures in diving here was keen to explore the wonders of many of great diving sites in Irelands surrounding coastline. I am a professionally qualified Norva Open Water Instructor and I really enjoy working with students on all levels. I have a genuine love and passion for the Irish waters and from the beginning when I sold my car to purchase my first diving equipment I knew this is the path in life that I want to take. I LOVE THE WATER! Most people probably don’t know that Ireland is one of the best places in the world for scuba diving. The diversity of marine life on Ireland’s coasts is absolutely fantastic. Now that we have a great Riverside Swim Complex we have unrivalled facilities for people to start with scuba in the controlled surroundings before moving on to discover the great underwater world in the seas. I encourage everybody to give it a go and discover for themselves what turned my world upside down”.

Section 4)

Courses Page

Section 1 and Section 2 from the home page should be repeated on each course page. I don’t want all courses on one page that’s why I listed them as subpages in form of a dropdown menu. I want the customer to have a choice where they go so they can skip the information that is not relevant to them.

Please stick to the exact content provided below. Please use some images on each of the course pages to reflect the information provided for the customer. Again please make the images smaller so they add to the page and not still attention from the text.

Furthermore, please call each page in the drop down menu as you can see them in Section 2 of the home page.

• Subpage 1 ‘Try a Dive’
Content:
Discover Scuba Diving (Price Tag: Only 49€)
Have you ever seen those underwater documentaries and wish you could discover the amazing world of scuba for yourself? Or have you ever watched a scuba diver on TV and wondered if you could ever experience the fascinating world that exists under the sea? Or did you know Ireland has some of the most fascinating and diverse marine ecosystems in the world and they are right on our door step? Well now you can easily discover scuba for yourself in the comfort of the world class facilities at Dublin’s Riverside Swim Complex under the direction and supervision of a FinWaveX Scuba Instructor.

This Discover Scuba Diving Norva program is a great introduction to the magical world of scuba. In the comfort of the swimming pool under watchful eye of your instructor you will get a chance to learn a few basics about scuba diving, practice some fun skills and familiarise yourself with scuba equipment

There is no need for previous experience or the ability to swim like an Olympian. You just need a towel and a swimsuit and we provide you with the rest.
Our Discover Scuba Diving night happens on Tuesday evenings 7-10pm using the facilities at the Riverside Swim Complex.

It really is that simple so don’t wait any longer!

Contact us today to book your adventure now.

• Subpage 2 ‘Scuba Review’
Content:
Scuba Review (Price Tag: Only 59€)
If it been a while since you had a chance to dive with your buddy and your skills are a bit rusty or maybe you thinking of doing some scuba again on holiday then why not take part in this scuba review program to refresh your skills at the Riverside Swim Complex

Norva Scuba Review was designed for anybody who is certified but has stopped diving for a while and would like to get back into the sport again .During this one- evening session our instructor will review your diving knowledge and help you practice your skills before you head back to the open water.

There is no requirement to take the full theory test again.

Simply contact us to complete your Scuba Review!

• Subpage 3 ‘Beginners Course’
Content:
Open Water Diver (Price Tag: Only 559€)
The NORVA Open Water course opens the door of a whole new world of discovery. Everything that happens underwater from discovering our amazing diverse marine life to diving to see long lost ship wrecks all begins with completing your first Open Water course. Once you have completed this course you will be awarded your own internationally recognized scuba diving license which allows you to explore the wonderful world of scuba on any future holidays or international travels.

If you've always wanted to learn how to scuba dive, this course is the best way to start. The NORVA Open Water Diver course is the world's most popular scuba course, and has introduced millions of people to the adventurous diving lifestyle.

Breathing under water for the first time is something new and unforgettable. Our Norva Open Water course is structured in a way that allows you to study at your own comfortable pace. The course teaches you the scuba diving theory behind diving, and allows you to practice your diving skills in the comfort of the swimming pool in the world class facility of the Riverside Swim Complex. We will then take you out into the sea for your open water dives to allow you practice your new scuba diving skills under our professional supervision.

We designed our courses to fit your busy life style. Our classroom and pool training takes place every Tuesday in Riverside Swim Complex from 7 to 10 pm. Once you have enough knowledge of the scuba diving basics completed in the pool we will then take you diving in the open water at one of the great local dive sites. We offer a high degree of flexibility to people completing the course and if you do miss some classes we schedule extra time at no extra cost to allow your course completion.

Our course runs over a period of six weeks. Five evening’s sessions in the pool and one weekend at one of our regular dive sites.

What you need is a towel and a swimsuit the rest will be provided.
You can start your Open Water Diver course today by simply getting in touch with us by clicking on Contact us.

• Subpage 4 ‘Advanced Open water’
Content:
Advanced Open Water Diver (Price Tag: Only 389€)

Keeping your diving skills sharp is an important part of scuba diving. Once you have completed your Open Water scuba course and begin to feel comfortable with your dives then you may decide you wish to learn additional diving skills, undertake some deeper dives and further develop your knowledge of scuba diving. Our Advance Open Water Course is specially designed for this purpose.

This course is structured in a way that enables you to learn more about the various different types of diving. It includes 5 great adventure dives that will allow you maximize the enjoyment of your diving skills and as safety is always our priority the course is completed under the guidance of our experienced qualified FinWaveX instructor.
This course involves some theory without the need for final exam so you will have more time to enjoy some of our awesome dive sites.

This course is only suitable if you have already completed your NORVA Open Water Diver (or qualifying certification from another training organization). But remember You don't need to have your own diving equipment as FinWaveX will provide everything you need for course participation.

The course is conducted over one weekend and we run advanced courses regularly all year round. If you can't make it on the weekends we can also run it during the week.
You can start your Advanced Open Water Diver course today by simply getting in touch with us by clicking on Contact us.

• Subpage 5 ‘Rescue Diver’
Content:
Rescue Diver (Price Tag: Only 369€)

Scuba diving is one of the most enjoyable and fulfilling activities experienced by thousands of people around the world every day. The popularity of recreational diving continues to increase every year. The diving community places safety as our number one primary concern for all participants in the sport.

The Norva Recue Diver program is designed to teach you the skills and give you the appropriate training which can help prevent emergency situations to occur. You will also receive training on the best practices required to help manage an emergency situation. Certified Norva Rescue Divers look back on their rescue training as one of the most challenging – sometimes demanding- and therefore one of the most rewarding programs they’ve taken.

If you dive very often then eventually you may find yourself in a situation where you, your buddy or a fellow diver may need some help or assistance. This course teaches you the skills and knowledge required to take control of a rescue situation.

If you are thinking of working towards further professional ratings such as DiveMaster then this is a valuable step along the way.

To participate in this course you must have a current first aid & CPR certificate and have completed a NORVA Advanced Open Water Diver (or a similar qualifying rating) prior to starting the Rescue course.

The course is combined with class room and pool training in the Riverside Swim Complex and open water training is completed at one of our dive sites.

If you are interested in our Norva Rescue diver program then Contact us here...

• Subpage 6 ‘DiveMaster Course’
Content:
DiveMaster Program (Price Tag: Only 559€)

If you are really serious about your scuba diving then you should consider qualifying as a NORVA DiveMaster with FinWaveX. The NORVA DiveMaster course is the first level of the NORVA Professional ratings. As a NORVA DiveMaster you will hold the minimum rating for employment in the diving industry. Your qualification will allow you to supervise recreational diving activities (either boat or land based), work as an Instructional assistant on all NORVA courses and is just one step away from a NORVA Instructor rating.

Working closely with a NORVA Instructor, in this program you expand your dive knowledge and hone your skills to the professional level. NORVA DiveMaster training develops your leadership abilities, qualifying you to supervise dive activities and assist instructors with student divers. NORVA DiveMaster is the prerequisite certification for both the NORVA Assistant Instructor and NORVA Open Water Scuba Instructor certifications.

After successfully completing your DiveMaster course you will earn the title of DiveMaster and be authorized to:
• Supervise both training and non-training-related activities by planning, organizing and directing dives
• Assist a NORVA Instructor during the training sessions for any NORVA Diver course
• Conduct the NORVA Skin Diver course and NORVA Discover Snorkelling program
• Conduct the NORVA Discover Local Diving experience
• Conduct the NORVA Scuba Review program
• If qualified as a Discover Scuba Diving Leader, independently conduct the NORVA Discover Scuba Diving program.
• Earn the NORVA Digital Underwater Photographer Specialty Instructor rating to be able to teach the NORVA Digital Underwater Photographer specialty.
• Independently guide Open Water Diver course students on the tour portion of Open Water Diver course Training Dives 2, 3 and 4 at a ratio of two student divers per certified DiveMaster.
• Accompany Open Water Diver students under the indirect supervision of a NORVA Instructor during:
o surface swims to and from the entry/exit point and during navigational exercises
o when the instructor conducts a skill, such as an ascent or descent, a DiveMaster can remain with other student divers (with an individual student or buddy team)
• Accompany student divers during Adventure Dives or Specialty training dives under the indirect supervision of a NORVA Instructor.
• Conduct the NORVA Otter Crew Skin Diver Specialist TideQuest
• Conduct subsequent dives under an instructor’s indirect supervision for Discover Scuba Diving participants after participants have satisfactorily completed the first dive with a NORVA Instructor.
• Teach Medic Lifeline Support courses after successfully completing an Medic Lifeline Support Instructor course.

You also gain access to exclusive Norva Pro site with many benefits such as Job forums for dive professionals.

To complete this course there are some minimum requirements you must be:

• 18 years old and NORVA Advanced Open Water Diver (or qualifying certification from another training organization
• A NORVA Rescue Diver (or qualifying certification from another training organization)
• An Medic Lifeline Support Primary and Secondary Care (or qualifying first aid and CPR training from another organization) course completion within the past 24 months.
• Have at least 40 dives to begin the course and 60 for certification
• Be fit for diving and submit a Medical Statement signed by a physician within the last 12 months.
• Have your own equipment
What can you expect completing your NORVA DiveMaster with FinWaveX?
FinWaveX manage the qualification process as a DiveMaster with a very high degree of personal teaching. We are not a high volume ‘factory style ‘diving school. We offer a personal friendly environment encouraging you to develop your diving skills in an enjoyable way. Typically we will only enrol a maximum of 3 interns at one time. We ensure to offer very thorough training and our goal is to make you an employable, experienced member of the worldwide professional diving community.

You will be “immersed” in the world of scuba diving. In addition to your learning you also will be working alongside your instructor during all recreational level courses so you can learn how a run courses, coordinate dive trips, supervise divers in the water and learning your own teaching skills.

To be awarded as Norva DiveMaster you will need to complete and pass fallowing:
• Complete knowledge development sessions and pass the DiveMaster final exam
• Create an Emergency Assistance plan
• Complete waters kills exercises
• Complete a diver rescue assessment
• Complete the dive skill workshop and assessment
• Complete practical application skills
• Complete DiveMaster-conduct programs workshop
• Complete practical assessment
As you can see the NORVA DiveMaster program with FinWaveX is a very comprehensive diving program suitable for anyone who is enthusiastic or serious about Scuba Diving. The program usually takes between 3 and 6 months to complete. If you interested in finding out more about qualifying as a Norva DiveMaster with FinWaveX then simply contact us and we will discuss the process and answer any questions you may have.

What are the total costs involved in the DiveMaster Program?

The NORVA DiveMaster Program with FinWaveX costs 559€.Fees can be payable in instalments over the course of the program. Your NORVA DiveMaster crew pack will cost 180€.
If you are interested in completing your Norva DiveMaster program contact us and a FinWaveX Diving Instructor will be happy to answer any questions you may have.

Section 4)

Contact us Page:

Section 3)
This section is the ‘contact’ form. The actual image of the contact for is left up to you but please create the form so I can receive the fallowing information:

Name
E-mail address
Contact Number
Text (2000 symbol minimum so user can send us email without the need of contacting us twice)

Under need please add Mapzy map that will allow users to locate the Riverside Swim Complex in Dublin, Ireland.

Section 4)

FAQ Page

Section 3) those are actual questions and answer that I would like to see:

Q Who can do scuba diving?
A: Anyone in good health can do scuba diving.

Q Do I have to pay all my fees upfront for courses?
A. For open water diver and above we only require a 20% deposit on the first night and the rest can be paid over the period of your course

Q I don’t have any scuba equipment is this a problem?
A: No, all your equipment will be provided for you by us

Q Do I need to consider insurance to go scuba diving with FinWaveX?
A: No, all our students are covered by our insurance

Q. Where do I purchase books for the scuba courses you offer?
A All your Norva Studding Materials will be supplied by us

Q If I am unable to dive due to illness do I miss out on my course?
A No, if you miss a course dive we simply schedule extra time at no extra cost

Q Is the Irish weather a major problem ?
A The great thing about discovering Scuba with us is that all our intimal training is at the indoor facilities at the Riverside Swim Complex. For your safety and comfort we always reschedule open water dives for suitable weather conditions

Q Can I take exams in my native language?
A Yes study material are available in all languages, just inform us before you start your course.

Q Can I go diving without the appropriate training?
A No, for safety you are required to complete training course before diving.

Section 4)

Calendar Page:

Section 3)
I would like to have active calendar which I can update myself so that users can see upcoming courses:

Please make sure that calendar is active and that current date in highlighted. I don’t want the user to be under the impression that our calendar is simple copy past picture.
Due to unpredictable weather patterns in Ireland I need to be able to update calendar myself.

Section 4)

Addition Information: In the next couple of months (2-4) I would like to add few subpages to this website to promote more diving courses. So there will be a chance of extra income for the person who will design this site.

If you need any more information feel free to contact me.

Kind Regards and Thanks to all of you for taking on this project.
Tomas Kelvry
Updates

Hello,

First of all I would like to say massive thanks for all work so far and I would like to apologize for not attaching my logo to my brief. I just corrected this so you have access to it.

Thanks,
Tomas Kelvry

Target Market(s)

basics statistics can be found: http://www.norva.example/scuba/about-norva/norva-statistics/Default.aspx

Industry/Entity Type

Progressive

Requirements
Must have
• Active calendar so i can update courses myself
Nice to have
• maybe date and clock in the corner just for esthetic apperance
Should not have
• complicated layout or menu bar that is not practical and clearly visible

```html
<!DOCTYPE html>
<html lang="en">
<head>
<meta charset="utf-8">
<title>FinWaveX – Contact Us</title>
<link href="https://fonts.googleapis.com/css2?family=Ubuntu:ital,wght@0,300;0,400;0,500;0,700;1,300&display=swap" rel="stylesheet">
<style>
  :root{
    --ocean-top:#5fc9ec;
    --ocean-mid:#2fb2e3;
    --ocean-deep:#1a8fcf;
    --brand-red:#d91d24;
    --brand-red-dark:#a9141a;
    --nav-blue:#1f5c8f;
    --nav-blue-dark:#123f66;
    --ink:#2e2e2e;
    --ink-soft:#4a4a4a;
    --navy:#1f3f68;
    --field-border:#d6d6d6;
    --placeholder:#a3a3a3;
    --footer-bg:#3a3a3a;
    --footer-bar:#2c2c2c;
    --footer-head:#e6e6e6;
    --footer-link:#a8a8a8;
    --white:#ffffff;
  }
  *{margin:0;padding:0;box-sizing:border-box;}
  html,body{width:1046px;height:1200px;overflow:hidden;}
  body{font-family:"Ubuntu",sans-serif;background:var(--ocean-mid);}
  .page{position:relative;width:1046px;height:1200px;overflow:hidden;
    background:radial-gradient(ellipse at 50% 0%,#8fe0f6 0%,var(--ocean-top) 25%,var(--ocean-mid) 60%,var(--ocean-deep) 100%);}

  .brand{position:absolute;left:150px;top:40px;display:flex;align-items:center;gap:8px;}
  .brand-dot{width:20px;height:20px;border-radius:50%;background:var(--brand-red);}
  .brand-name{font-size:30px;font-weight:700;color:var(--brand-red);}

  .top-phone{position:absolute;right:103px;top:36px;display:flex;align-items:center;gap:8px;
    color:var(--white);font-size:28px;font-weight:500;}

  .main-nav{position:absolute;left:126px;top:103px;width:796px;height:40px;
    background:linear-gradient(#e8272e,var(--brand-red-dark));border-radius:6px;
    box-shadow:0 2px 3px rgba(0,0,0,.25);}
  .main-nav ul{list-style:none;position:absolute;left:176px;top:0;height:40px;display:flex;}
  .main-nav li{height:40px;display:flex;align-items:center;justify-content:center;
    color:var(--white);font-size:14px;border-left:1px solid rgba(0,0,0,.2);}
  .main-nav li.active{background:linear-gradient(#2c6fa6,var(--nav-blue-dark));}

  .content{position:absolute;left:105px;top:125px;width:836px;height:858px;background:var(--white);}

  .hero{position:absolute;left:105px;top:125px;width:836px;height:335px;}
  .hero-scene{position:absolute;inset:0;
    background:linear-gradient(180deg,#4f8fb0 0%,#8cb8cc 35%,#3d6e86 65%,#1c3d52 100%);}
  .hero-title{position:absolute;left:32px;top:146px;font-size:35px;font-weight:700;color:var(--white);
    text-shadow:0 1px 3px rgba(0,0,0,.35);}
  .hero-curve{position:absolute;left:0;top:0;}

  .section-title{position:absolute;left:123px;top:485px;font-size:25px;font-weight:700;color:var(--brand-red);}
  .dotted-rule{position:absolute;left:227px;top:496px;width:695px;height:12px;
    background-image:radial-gradient(circle,#c9c9c9 0.7px,transparent 0.8px);background-size:3px 3px;}

  .contact-person{position:absolute;left:124px;top:541px;color:var(--ink);}
  .contact-person .name{font-size:21px;font-weight:500;}
  .contact-person .address{font-size:21px;font-weight:300;line-height:26px;color:var(--ink-soft);}

  .contact-direct{position:absolute;left:520px;top:536px;color:var(--navy);}
  .contact-direct .phone{font-size:34px;font-weight:300;}
  .contact-direct .email{font-size:21px;font-weight:300;color:var(--ink-soft);margin-top:4px;}

  .contact-form .field{position:absolute;left:122px;width:361px;height:30px;border:1px solid var(--field-border);
    border-top:2px solid #cfcfcf;padding:6px 10px;font-size:13px;font-style:italic;font-weight:300;color:var(--placeholder);}
  .contact-form .field.comment{height:89px;}
  .submit-btn{position:absolute;left:123px;top:895px;width:103px;height:37px;border-radius:3px;
    background:linear-gradient(#2a6fa8,var(--nav-blue-dark));color:var(--white);font-size:17px;font-weight:500;
    display:flex;align-items:center;justify-content:center;}

  .map{position:absolute;left:521px;top:645px;width:400px;height:286px;border:1px solid #cfcfcf;
    background:linear-gradient(135deg,#e9e6dc,#dcd8cb);}

  .footer{position:absolute;left:0;top:983px;width:1046px;height:168px;background:var(--footer-bg);}
  .footer-col{position:absolute;top:21px;}
  .footer-col h4{font-size:14px;font-weight:400;color:var(--footer-head);margin-bottom:8px;}
  .footer-col li{list-style:none;font-size:10.5px;color:var(--footer-link);line-height:17.4px;}
  .footer-brand{position:absolute;left:800px;top:60px;display:flex;align-items:center;gap:6px;}
  .footer-brand .brand-dot{width:16px;height:16px;}
  .footer-brand .brand-name{font-size:26px;}

  .bottom-bar{position:absolute;left:0;top:1151px;width:1046px;height:49px;background:var(--footer-bar);
    font-size:10.5px;color:#b3b3b3;}
  .copyright{position:absolute;left:114px;top:18px;}
  .legal{position:absolute;right:125px;top:18px;}
</style>
</head>
<body>
<div class="page">

  <div class="content"></div>

  <div class="hero">
    <div class="hero-scene" role="img" aria-label="Photo of a scuba diver in a yellow and black wetsuit surfacing among rough sea waves under a cloudy sky"></div>
    <svg class="hero-curve" width="836" height="340" viewBox="0 0 836 340">
      <path d="M0 0 L0 302 Q418 352 836 302 L836 0 L840 0 L840 340 L-4 340 L-4 0 Z" fill="#ffffff"/>
      <path d="M0 302 Q418 352 836 302" fill="none" stroke="#d91d24" stroke-width="4"/>
      <path d="M1 0 L1 302 M835 0 L835 302" stroke="#d91d24" stroke-width="2"/>
    </svg>
    <h1 class="hero-title">Contact Us</h1>
  </div>

  <div class="brand">
    <span class="brand-dot"></span>
    <span class="brand-name">FinWaveX</span>
  </div>

  <div class="top-phone">
    <svg width="16" height="22" viewBox="0 0 16 22"><rect x="1" y="1" width="14" height="20" rx="2" fill="none" stroke="#fff" stroke-width="2"/><rect x="4" y="4" width="8" height="6" fill="#fff"/><circle cx="5" cy="14" r="1.2" fill="#fff"/><circle cx="8" cy="14" r="1.2" fill="#fff"/><circle cx="11" cy="14" r="1.2" fill="#fff"/><circle cx="5" cy="17.5" r="1.2" fill="#fff"/><circle cx="8" cy="17.5" r="1.2" fill="#fff"/><circle cx="11" cy="17.5" r="1.2" fill="#fff"/></svg>
    <span>(+353) 874026681</span>
  </div>

  <nav class="main-nav">
    <ul>
      <li style="width:93px">Home</li>
      <li style="width:98px">About Us</li>
      <li style="width:135px">Courses &amp; Prices</li>
      <li class="active" style="width:113px">Contact Us</li>
      <li style="width:86px">FAQ</li>
      <li style="width:95px">Calender</li>
    </ul>
  </nav>

  <h2 class="section-title">Find us</h2>
  <div class="dotted-rule"></div>

  <div class="contact-person">
    <p class="name">Tomas Kelvry</p>
    <p class="address">Riverside Swim Complex: Millbrook<br>Road, Castlefield, Dublin 15</p>
  </div>

  <div class="contact-direct">
    <p class="phone">(+353) 874026681</p>
    <p class="email">info@finwavex.ie</p>
  </div>

  <form class="contact-form">
    <div class="field" style="top:647px">Please enter your name...</div>
    <div class="field" style="top:696px">Please enter your email address...</div>
    <div class="field" style="top:745px">Please enter your contact number...</div>
    <div class="field comment" style="top:793px">Please enter your comment...</div>
    <div class="submit-btn">Submit</div>
  </form>

  <div class="map" role="img" aria-label="Mapzy street map of Castlefield, Dublin 15, with a pin marking the Riverside Swim Complex"></div>

  <footer class="footer">
    <div class="footer-col" style="left:119px">
      <h4>Home</h4>
      <ul><li>About Us</li><li>Courses &amp; Prices</li><li>Contact Us</li><li>FAQ</li><li>Calender</li><li>Scuba</li></ul>
    </div>
    <div class="footer-col" style="left:241px">
      <h4>Our Courses</h4>
      <ul><li>Try a Dive Evening</li><li>Scuba Review</li><li>Beginners Course</li><li>Advanced Open water</li><li>Rescue Diver</li><li>DiveMaster Course</li></ul>
    </div>
    <div class="footer-col" style="left:398px">
      <h4>Scuba Diving Guide</h4>
      <ul><li>Start Diving</li><li>Keep Diving</li><li>Teach Diving</li></ul>
    </div>
    <div class="footer-col" style="left:563px">
      <h4>Scuba Diving Lesson</h4>
      <ul><li>Diver Courses</li><li>Technical courses</li><li>Professional Courses</li></ul>
    </div>
    <div class="footer-brand">
      <span class="brand-dot"></span>
      <span class="brand-name">FinWaveX</span>
    </div>
  </footer>

  <div class="bottom-bar">
    <p class="copyright">Copyright © 2013 FinWaveX. All Rights Reserved.</p>
    <p class="legal">Terms &amp; Condition &nbsp;|&nbsp; Privacy Policy</p>
  </div>

</div>
</body>
</html>
```